Tervoli Pizza & Pasta Takeaway Flyer

Our takeaway shop needs a well designed flyer for print and letter box distribution. Design to have a clear list of menu, Specials, contact details. If menu doesn't fit into A4, we won't mind going upto extended A4. I have attached draft copy of our menu and list of item in excel. Please add 5mm Bleed to the flyer.
Flyer will get printed on 115gsm Gloss stock.

Industry/Entity Type

Hospitality

```html
<!DOCTYPE html>
<html lang="en">
<head>
<meta charset="utf-8">
<title>Tervoli Pizza &amp; Pasta – Takeaway Menu</title>
<link href="https://fonts.googleapis.com/css2?family=Righteous&family=Open+Sans:wght@400;600;700&family=Oswald:wght@400;500&display=swap" rel="stylesheet">
<style>
:root{
  --green:#7cc242;
  --green-dark:#4f8f1f;
  --red:#c8161d;
  --red-dark:#6e0a0d;
  --black:#111;
  --charcoal:#232323;
  --white:#fff;
  --text-soft:#d8d8d8;
  --stage:#e6e6e6;
}
*{box-sizing:border-box;margin:0;padding:0}
html,body{width:1200px;height:762px;overflow:hidden;background:var(--stage)}
.brochure{position:absolute;left:30px;top:30px;width:1140px;height:702px;display:flex;overflow:hidden;box-shadow:0 4px 14px rgba(0,0,0,.25)}
.panel{position:relative;width:285px;height:702px;padding:18px 20px 0}
.panel--green{background:linear-gradient(160deg,var(--green) 0%,#6cb332 60%,var(--green-dark) 100%)}
.panel--dark{background:linear-gradient(180deg,#2a2a2a 0%,var(--charcoal) 50%,#151515 100%)}
.panel--red{background:linear-gradient(180deg,var(--red) 0%,#a31217 55%,var(--red-dark) 100%)}
.panel--cover{background:linear-gradient(180deg,#2b2b2b,#141414)}

.heading{font-family:"Righteous",sans-serif;font-size:19px;letter-spacing:.5px;text-align:center;border-radius:14px;padding:2px 0 1px;margin:0 14px 8px}
.heading--black{background:var(--black);color:var(--white)}
.heading--green{background:var(--green);color:var(--black)}
.heading .heading__price{color:var(--red)}
.subnote{font-family:"Open Sans",sans-serif;font-size:8px;color:var(--black);text-align:center;margin:-5px 0 6px}

.menu{list-style:none;margin-bottom:12px}
.menu__item{display:flex;justify-content:space-between;align-items:baseline;margin-bottom:4px}
.menu__text{flex:1;padding-right:8px}
.menu__name{font-family:"Righteous",sans-serif;font-size:11.5px;color:var(--white);text-transform:uppercase;letter-spacing:.3px;line-height:1.15}
.menu__desc{font-family:"Open Sans",sans-serif;font-size:7.2px;line-height:1.2;color:var(--white)}
.panel--dark .menu__desc{color:#bdbdbd}
.menu__price{font-family:"Righteous",sans-serif;font-size:11.5px;color:var(--white)}

.delivery{font-family:"Open Sans",sans-serif;font-weight:700;font-size:11px;color:var(--black);text-align:center;border-bottom:1px solid var(--black);padding-bottom:2px;margin:0 4px 8px}
.delivery span{color:var(--white)}
.deals{list-style:none}
.deals .menu__item{margin-bottom:6px}
.deals .menu__name{display:flex;gap:6px;align-items:center}
.deals .menu__name::before{content:"";width:5px;height:5px;border-radius:50%;background:var(--black);flex:none}
.deals .menu__desc{padding-left:11px;font-size:8px}
.divider{height:1px;background:var(--white);margin:10px 14px 14px}
.contact__title{font-family:"Righteous",sans-serif;font-size:12px;color:var(--white);margin-bottom:4px}
.contact__line{display:flex;gap:5px;align-items:flex-start;font-family:"Open Sans",sans-serif;font-size:8.5px;font-weight:600;color:var(--white);line-height:1.25;margin-bottom:3px}
.contact__line svg{flex:none;margin-top:1px}

.pizza-band{position:absolute;left:560px;top:420px;width:600px;height:600px;border-radius:50%;background:var(--black);border:10px solid var(--red)}
.pizza-photo{position:absolute;left:630px;top:440px;width:450px;height:450px;border-radius:50%;background:radial-gradient(circle at 45% 40%,#f6e7b8 0%,#e9c879 45%,#d29c4a 70%,#b7b2a8 72%,#dedbd4 100%)}
.map{position:absolute;left:583px;top:473px;width:124px;height:124px;border-radius:50%;background:linear-gradient(135deg,#e9e4d6,#cfd8c4);border:5px solid var(--white);box-shadow:0 0 0 3px var(--red)}
.web{position:absolute;top:632px;height:24px;border-radius:12px;background:var(--white);font-family:"Open Sans",sans-serif;font-weight:700;font-size:11.5px;color:var(--black);display:flex;align-items:center;justify-content:center}
.web--inside{left:624px;width:200px}
.web--cover{left:897px;width:196px}

.brand{position:absolute;left:905px;top:12px;width:170px;height:170px;border-radius:50%;border:3px solid var(--red);display:flex;flex-direction:column;align-items:center;justify-content:center}
.brand__name{font-family:"Righteous",sans-serif;font-size:34px;color:var(--green);line-height:1}
.brand__tag{font-family:"Open Sans",sans-serif;font-size:12px;color:var(--white);margin-top:6px}
.cover-rule{position:absolute;left:870px;top:250px;width:240px;height:2px;background:var(--red)}
.cover-title{position:absolute;left:855px;width:285px;text-align:center;font-family:"Oswald",sans-serif;line-height:1}
.cover-title--red{top:258px;font-size:30px;color:var(--red);letter-spacing:1px}
.cover-title--white{top:294px;font-size:22px;color:var(--white);letter-spacing:1.5px}
.dish{position:absolute;border-radius:50%;border:5px solid var(--white);box-shadow:0 0 0 3px var(--red)}
.dish--pasta{left:897px;top:362px;width:96px;height:96px;background:radial-gradient(circle,#e0a64f,#9b4b1d 70%,#f1f1f1 72%)}
.dish--ribs{left:1003px;top:377px;width:116px;height:116px;background:radial-gradient(circle at 50% 55%,#8a4b22,#5a2a12 55%,#e9e5dc 60%,#c9c2b6)}
</style>
</head>
<body>
<main class="brochure">

  <section class="panel panel--green">
    <h2 class="heading heading--black">RIBS &amp; WINGS</h2>
    <ul class="menu">
      <li class="menu__item"><div class="menu__text"><div class="menu__name">Pork Ribs</div></div><span class="menu__price">$17</span></li>
      <li class="menu__item"><div class="menu__text"><div class="menu__name">Beef Ribs</div></div><span class="menu__price">$15</span></li>
      <li class="menu__item"><div class="menu__text"><div class="menu__name">Buffalo Wings(6 pcs)</div></div><span class="menu__price">$8</span></li>
      <li class="menu__item"><div class="menu__text"><div class="menu__name">BBQ Wings(6 pcs)</div></div><span class="menu__price">$8</span></li>
      <li class="menu__item"><div class="menu__text"><div class="menu__name">Honey Soy Wings(6 pcs)</div></div><span class="menu__price">$8</span></li>
      <li class="menu__item"><div class="menu__text"><div class="menu__name">Fried Wings (6 pcs)</div><div class="menu__desc">with Tomato Sauce</div></div><span class="menu__price">$8</span></li>
      <li class="menu__item"><div class="menu__text"><div class="menu__name">Chicken Lollipop(5 pcs)</div><div class="menu__desc">With Lemon Wedges</div></div><span class="menu__price">$8</span></li>
    </ul>

    <h2 class="heading heading--black">THE AB</h2>
    <p class="subnote">[Chips Topped with Cheese, Meat, Veg &amp; Sauces]</p>
    <ul class="menu">
      <li class="menu__item"><div class="menu__text"><div class="menu__name">AB Chicken</div><div class="menu__desc">Marinated Chicken,Cheese on Top of Fries, Drizzled with Ranch, BBQ &amp; Garlic Sauce</div></div><span class="menu__price">$13.95</span></li>
      <li class="menu__item"><div class="menu__text"><div class="menu__name">AB Meat L</div><div class="menu__desc">Cheese, Pulled Beef, Bacon, Ham on Top of Fries, Drizzled with Ranch, BBQ &amp; Garlic Sauce</div></div><span class="menu__price">$13.95</span></li>
      <li class="menu__item"><div class="menu__text"><div class="menu__name">AB Combi</div><div class="menu__desc">Cheese, Chicken, Pulled Beef, Ham on Top of Fries, Drizzled with Ranch, BBQ &amp; Garlic Sauce</div></div><span class="menu__price">$13.95</span></li>
      <li class="menu__item"><div class="menu__text"><div class="menu__name">AB Veg</div><div class="menu__desc">Cheese, Tomato, Capsicum, Mushroom, crumbed Fetta, Pineapple on Top of Fries, Drizzled with Ranch, Tomato &amp; Garlic Sauce</div></div><span class="menu__price">$13.95</span></li>
      <li class="menu__item"><div class="menu__text"><div class="menu__name">AB Doubl</div><div class="menu__desc">Double Cheese on Top of Fries, Drizzled with Ranch, Tomato &amp; Garlic Sauce</div></div><span class="menu__price">$11.95</span></li>
    </ul>

    <h2 class="heading heading--black">SALAD</h2>
    <ul class="menu">
      <li class="menu__item"><div class="menu__text"><div class="menu__name">Garden Salad</div><div class="menu__desc">Mixed Leaves, Tomato, Cucumber, Olives, Onion, Capsicum, Pineapple &amp; Italian dressing</div></div><span class="menu__price">$6</span></li>
      <li class="menu__item"><div class="menu__text"><div class="menu__name">Greek Salad</div><div class="menu__desc">Mixed Leaves, Tomato, Cucumber, Olives, Onion, Fetta &amp; Dressed with Lemon Juice, Olive Oil, White wine vinegar</div></div><span class="menu__price">$6</span></li>
      <li class="menu__item"><div class="menu__text"><div class="menu__name">Coleslaw</div><div class="menu__desc">Red Cabbage, Green Cabbage, Carrot, Onion mixed with Mayonnaise and Lemon</div></div><span class="menu__price">$6</span></li>
      <li class="menu__item"><div class="menu__text"><div class="menu__name">Chicken Ceaser Salad</div><div class="menu__desc">Mixed Leaves, Chicken, Crispy Bacon, Croutons, Parmesan Cheese &amp; Ceaser Dressing</div></div><span class="menu__price">$9</span></li>
    </ul>
  </section>

  <section class="panel panel--dark">
    <h2 class="heading heading--green">DRINKS</h2>
    <ul class="menu">
      <li class="menu__item"><div class="menu__text"><div class="menu__name">Can</div><div class="menu__desc">Cola, Diet Cola, Cola Zero, Orange Fizz, Lemon Fizz</div></div><span class="menu__price">$2.95</span></li>
      <li class="menu__item"><div class="menu__text"><div class="menu__name">1.25 Lit</div><div class="menu__desc">Cola, Diet Cola, Cola Zero, Orange Fizz, Lemon Fizz</div></div><span class="menu__price">$4.95</span></li>
      <li class="menu__item"><div class="menu__text"><div class="menu__name">Leafton Ice Tea</div></div><span class="menu__price">$3.95</span></li>
      <li class="menu__item"><div class="menu__text"><div class="menu__name">Orange Juice</div></div><span class="menu__price">$4.50</span></li>
      <li class="menu__item"><div class="menu__text"><div class="menu__name">Ginger Beer</div></div><span class="menu__price">$3.95</span></li>
      <li class="menu__item"><div class="menu__text"><div class="menu__name">Mount Carrow Water</div></div><span class="menu__price">$2.50</span></li>
      <li class="menu__item"><div class="menu__text"><div class="menu__name">Rally Energy Drink</div><div class="menu__desc">(375 ml)</div></div><span class="menu__price">$3.95</span></li>
    </ul>

    <h2 class="heading heading--green">DESSERT</h2>
    <ul class="menu">
      <li class="menu__item"><div class="menu__text"><div class="menu__name">Chocolate Sundae</div></div><span class="menu__price">$4.95</span></li>
      <li class="menu__item"><div class="menu__text"><div class="menu__name">Hazelo Calzone</div><div class="menu__desc">Calzone filled with Hazelo &amp; topped with Icing Sugar</div></div><span class="menu__price">$6</span></li>
      <li class="menu__item"><div class="menu__text"><div class="menu__name">Berry Zone</div><div class="menu__desc">Hazelo Calzone filled with Mixed Berry &amp; topped with Icing Sugar</div></div><span class="menu__price">$9</span></li>
      <li class="menu__item"><div class="menu__text"><div class="menu__name">White Valcone</div><div class="menu__desc">Calzone filled with White Chocolate &amp; topped with Icing Sugar</div></div><span class="menu__price">$9</span></li>
      <li class="menu__item"><div class="menu__text"><div class="menu__name">Crumbo Calzone</div><div class="menu__desc">Calzone rolled with Crumbo, filled with White Chocolate &amp; topped with Icing Sugar</div></div><span class="menu__price">$9</span></li>
      <li class="menu__item"><div class="menu__text"><div class="menu__name">Tropical Calzone</div><div class="menu__desc">Hazelo Calzone filled with Mango and Pineapple &amp; topped with Icing Sugar</div></div><span class="menu__price">$9</span></li>
    </ul>

    <h2 class="heading heading--green">DINNER PACK <span class="heading__price">$25</span></h2>
    <ul class="menu">
      <li class="menu__item"><div class="menu__text"><div class="menu__name">Pizza Pack</div><div class="menu__desc">Cheesy Garlic Bread, Any Large Pizza (Excl Premium range), Any Dessert or 1.25 lit</div></div><span class="menu__price">$4.95</span></li>
      <li class="menu__item"><div class="menu__text"><div class="menu__name">Pasta Pack</div><div class="menu__desc">Curly Fries, Any Pasta, Any Dessert or 1.25 lit</div></div><span class="menu__price">$6</span></li>
      <li class="menu__item"><div class="menu__text"><div class="menu__name">Parmi Pack</div><div class="menu__desc">Chips, Any Parmigiana, Any Dessert or 1.25 lit</div></div><span class="menu__price">$9</span></li>
      <li class="menu__item"><div class="menu__text"><div class="menu__name">Ribs &amp; Wings Pack</div><div class="menu__desc">Chips, Any Wings, Ribs (Pork or Beef)</div></div><span class="menu__price">$9</span></li>
    </ul>
  </section>

  <section class="panel panel--red">
    <h2 class="heading heading--black">DEALS</h2>
    <p class="delivery">FREE DELIVERY <span>$40 AND OVER</span></p>
    <ul class="deals">
      <li class="menu__item"><div class="menu__text"><div class="menu__name">Party Deal</div><div class="menu__desc">3 Large Pizza or Pasta, 2 Garlic Bread &amp; 1.25 lit Drink</div></div><span class="menu__price">$54.95</span></li>
      <li class="menu__item"><div class="menu__text"><div class="menu__name">Family Deal</div><div class="menu__desc">2 Large Pizza or Pasta, 2 Garlic Bread, 1.25 lit drink</div></div><span class="menu__price">$39.95</span></li>
      <li class="menu__item"><div class="menu__text"><div class="menu__name">Couple Deal</div><div class="menu__desc">1 Family Pizza, 1 Garlic Bread, 1.25 lit Drink</div></div><span class="menu__price">$24.95</span></li>
      <li class="menu__item"><div class="menu__text"><div class="menu__name">Single Deal</div><div class="menu__desc">1 Large Pizza or Pasta, 1 Garlic Bread, 1 can drink</div></div><span class="menu__price">$19.95</span></li>
      <li class="menu__item"><div class="menu__text"><div class="menu__name">Small Deal</div><div class="menu__desc">1 Small Pizza, 1 Garlic Bread, 1 can drink - $14.95</div></div><span class="menu__price">$14.95</span></li>
      <li class="menu__item"><div class="menu__text"><div class="menu__name">Terms &amp; Condition</div><div class="menu__desc">(Large Pizza Excludes Premium &amp; Seafood range, One Offer per order)</div></div></li>
    </ul>
    <div class="divider"></div>
    <div class="contact">
      <h3 class="contact__title">CONTACT</h3>
      <p class="contact__line"><svg width="8" height="10" viewBox="0 0 8 10"><path d="M4 0a4 4 0 0 0-4 4c0 3 4 6 4 6s4-3 4-6a4 4 0 0 0-4-4zm0 5.5A1.5 1.5 0 1 1 4 2.5a1.5 1.5 0 0 1 0 3z" fill="#fff"/></svg><span>Tervoli Pizza &amp; Pasta,<br>142 Harlow Rd,<br>Brenfield</span></p>
      <p class="contact__line"><svg width="9" height="9" viewBox="0 0 10 10"><circle cx="5" cy="5" r="4.4" fill="none" stroke="#fff" stroke-width="1"/><path d="M3.3 2.6l1 1-.5.7c.4.8 1 1.4 1.8 1.8l.7-.5 1 1-.7.8C4.9 7.2 2.8 5.1 2.6 3.3z" fill="#fff"/></svg><span>07 5550 1427</span></p>
    </div>
  </section>

  <section class="panel panel--cover"></section>

  <div class="pizza-band" aria-hidden="true"></div>
  <div class="pizza-photo" role="img" aria-label="Photo of a cheese pizza topped with red capsicum and parsley on a white plate"></div>
  <div class="map" role="img" aria-label="Street map showing the shop location"></div>
  <div class="web web--inside">www.tervoli.com.au</div>

  <div class="brand">
    <span class="brand__name">Tervoli</span>
    <span class="brand__tag">Pizza &amp; Pasta</span>
  </div>
  <div class="cover-rule"></div>
  <h1 class="cover-title cover-title--red">RESTAURANT</h1>
  <p class="cover-title cover-title--white">MENU</p>
  <div class="dish dish--pasta" role="img" aria-label="Photo of a plate of pasta"></div>
  <div class="dish dish--ribs" role="img" aria-label="Photo of grilled ribs with sauce"></div>
  <div class="web web--cover">www.tervoli.com.au</div>
</main>
</body>
</html>
```